'TOLVANTA' NEW WINE LABEL DESIGN

I am looking for an exceptional and exciting design for a wine label called 'Tolvanta' meaning 'Lookout'. The design must feature the name 'Tolvanta', and the word 'Cabernet Sauvignon' in version 1 and 'Sauvignon Blanc' in version 2. It will also need the words 'Valle Central, Chile' at the bottom of the label as a prominent piece of information as well as the vintage 2017. Please produce the work in size 80mm x 100mm. Feel free to use colour in addition to black/white and ensue that the label is easy to read on a shelf placement.
Target Market(s)
SUPERMARKETS & WINE STORES
Requirements
Must have
- EASY TO READ, USE COLOURS LIKE GREEN FOR SAUVIGNON & RED FOR CABERNET SAUVIGNON
- FULL BOTTLE SHOT MUST BE IN PROVIDED DESIGNS. ALL BOTTLE TOPS SHOULD BE QUORLAN STYLE (SCREW TOP)
- PLEASE NOTE THAT LABEL INFORMATION MUSY BE EASY TO READ I.E. VINTAGE, PLACE OF ORGIN ALTHOUGH NOT THE MAIN CONTENT MUST STILL BE CLEAR.
Nice to have
- ARTISTIC REFERENCE LINK TO NAME & ANDES BUT NOT PICTURES OF MOUNTAINS
Should not have
- PICTURES OF GRAPES
- PICTURES OF VINEYARDS
- PICTURES OF MOUNTAINS

```html
<!DOCTYPE html>
<html lang="en">
<head>
<meta charset="utf-8">
<title>Tolvanta Wine Labels</title>
<link href="https://fonts.googleapis.com/css2?family=Antic+Didone&family=Cinzel:wght@400;600&family=Pinyon+Script&display=swap" rel="stylesheet">
<style>
  :root {
    --backdrop: #dfe6ec;
    --label-black: #141414;
    --label-text: #ffffff;
    --cabernet-red: #e8322f;
    --sauvignon-green: #9ccb3b;
  }
  * { margin: 0; padding: 0; box-sizing: border-box; }
  html, body {
    width: 1200px;
    height: 1200px;
    overflow: hidden;
    background: var(--backdrop);
  }
  .label-set {
    width: 1200px;
    height: 1200px;
    display: flex;
    justify-content: center;
    align-items: center;
    gap: 100px;
  }
  .wine-label {
    width: 440px;
    height: 560px;
    background: var(--label-black);
    color: var(--label-text);
    display: flex;
    flex-direction: column;
    align-items: center;
    padding-top: 60px;
    box-shadow: 0 10px 30px rgba(0,0,0,0.18);
  }
  .wine-label--red { --accent: var(--cabernet-red); }
  .wine-label--green { --accent: var(--sauvignon-green); }
  .brand-square {
    width: 116px;
    height: 116px;
    background: var(--accent);
  }
  .brand-name {
    margin-top: 42px;
    font-family: "Antic Didone", serif;
    font-size: 98px;
    line-height: 1;
    letter-spacing: 0;
    transform: scaleX(0.72);
    font-weight: 400;
  }
  .variety-band {
    width: 100%;
    margin-top: 6px;
    background: var(--accent);
    text-align: center;
    font-family: "Cinzel", serif;
    font-size: 20px;
    font-weight: 600;
    letter-spacing: 4px;
    line-height: 32px;
    color: var(--label-text);
  }
  .vintage {
    margin-top: 80px;
    font-family: "Cinzel", serif;
    font-size: 26px;
    letter-spacing: 4px;
  }
  .origin {
    margin-top: 6px;
    font-family: "Pinyon Script", cursive;
    font-size: 34px;
  }
</style>
</head>
<body>
  <main class="label-set">
    <section class="wine-label wine-label--red">
      <div class="brand-square"></div>
      <h1 class="brand-name">TOLVANTA</h1>
      <p class="variety-band">CABERNET SAUVIGNON</p>
      <p class="vintage">2017</p>
      <p class="origin">Valle Central, Chile</p>
    </section>
    <section class="wine-label wine-label--green">
      <div class="brand-square"></div>
      <h1 class="brand-name">TOLVANTA</h1>
      <p class="variety-band">SAUVIGNON BLANC</p>
      <p class="vintage">2017</p>
      <p class="origin">Valle Central, Chile</p>
    </section>
  </main>
</body>
</html>
```